We need our website look and feel updated to match our brand

We are looking to update our website and a "where to buy" tab at the top of the website. The current look and feel is ok but needs a clean up. The task is as follows:
1. Update the current pages and add a page for "Where to Buy"
2. Update the product page to reflect our current products. ie we have only three products now. Undercoat K, Undercoat M and GLAZEX. This page will have very similar descriptions and at the bottom of each product will be a link to our SDS (safety data sheets).
3. Please visit our current website for the look and feel.
4. Use our New Taglines need to be included. "Always Cleaning. All the Time." "24/7 SAFE SURFACE PROTECTION" (Logo as well)
5. The HomePage will need a nice clean location to our corporate video. https://clipvue.net/8kRtWmPzQaL (link for viewing) that will be the highlight and easy to access on the homepage.
Some examples of websites we like.
https://velmarix.com/
https://quorbelhall.com/ (like the use of motion graphics in these)
Our focus claims are that our product is a surface cleaner and deodorizer. We would like to see variations in black, white background (Black header bar) and Gray backgrounds.

```html
<!DOCTYPE html>
<html lang="en">
<head>
<meta charset="utf-8">
<title>About Us – Veralith</title>
<link href="https://fonts.googleapis.com/css2?family=Questrial&display=swap" rel="stylesheet">
<style>
:root{
  --yellow:#f6c400;
  --dark:#333333;
  --ink:#1c1c1c;
  --body:#555555;
  --grey:#f2f2f2;
  --line:#d9d9d9;
  --white:#ffffff;
}
*{box-sizing:border-box;margin:0;padding:0}
html,body{width:1200px;height:3259px;overflow:hidden}
body{font-family:"Questrial",sans-serif;color:var(--ink);background:var(--white);position:relative}
.abs{position:absolute}
p{font-size:14px;line-height:24.5px;color:var(--body);letter-spacing:.2px}

/* header */
.site-header{left:0;top:0;width:1200px;height:86px;background:var(--dark)}
.brand{left:162px;top:26px;display:flex;align-items:center;gap:8px}
.brand-square{width:14px;height:14px;background:var(--yellow)}
.brand-name{color:var(--white);font-size:30px;line-height:32px}
.main-nav{left:330px;top:35px;display:flex;align-items:center;font-size:13.5px;color:var(--white)}
.main-nav span{padding:0 10px;border-left:1px solid #888;line-height:14px}
.main-nav span:first-child{border-left:none}
.main-nav .active{color:var(--yellow);position:relative}
.main-nav .active::after{content:"";position:absolute;left:5px;right:5px;top:25px;height:3px;background:var(--yellow)}
.search-tab{left:880px;top:0;width:30px;height:108px;background:var(--yellow);border-radius:0 0 15px 15px}
.search-tab .label{position:absolute;left:7px;top:22px;writing-mode:vertical-rl;transform:rotate(180deg);font-size:13px;line-height:16px;color:var(--ink)}
.search-tab .icon{position:absolute;left:5px;top:82px;width:20px;height:20px;border-radius:50%;background:var(--dark)}
.buy-btn{left:927px;top:24px;width:111px;height:35px;border:1.5px solid var(--yellow);border-radius:18px;color:var(--yellow);font-size:13.5px;display:flex;align-items:center;justify-content:center}

/* hero */
.hero{left:0;top:86px;width:1200px;height:299px;background:linear-gradient(90deg,#cf8fb8 0%,#c4b1c6 25%,#b5cbd4 55%,#9fc0d8 100%)}
.hero h1{position:absolute;left:162px;top:122px;font-size:42px;font-weight:400;color:var(--white)}
.crumbs{left:162px;top:405px;font-size:13px;color:var(--ink)}
.crumbs b{font-weight:400;color:#999;margin:0 10px}

/* about */
.grey-band{left:0;top:960px;width:1200px;height:573px;background:var(--grey)}
.about-photo{left:162px;top:477px;width:386px;height:526px;background:linear-gradient(160deg,#8e9aa6,#d7dde3 45%,#7f8b96)}
.eyebrow{font-size:13px;color:var(--ink);letter-spacing:.3px}
.title{display:flex;align-items:center;position:relative;font-size:34px;font-weight:400;color:var(--ink)}
.title::before{content:"";position:absolute;left:0;top:0;width:50px;height:100%;border:4px solid var(--yellow);border-right:none}
.title span{position:relative;padding-left:17px}
.about-text{left:591px;top:488px;width:446px}
.about-text .title{height:56px;margin:8px 0 18px}
.about-text p{margin-bottom:10px}
.col-left{left:163px;top:1053px;width:416px}
.col-right{left:622px;top:1053px;width:415px}
.col-left p,.col-right p{margin-bottom:16px}

/* features */
.features{left:162px;top:1623px;display:flex;gap:22px}
.card{width:203px;height:239px;background:var(--white);box-shadow:0 0 18px rgba(0,0,0,.08);text-align:center;padding-top:36px}
.card .badge{width:79px;height:79px;border-radius:50%;background:var(--yellow);margin:0 auto 24px;display:flex;align-items:center;justify-content:center}
.card small{display:block;font-size:12.5px;color:var(--ink);margin-bottom:8px}
.card strong{display:block;font-weight:400;font-size:16.5px;line-height:21px;color:var(--ink);padding:0 18px}

/* team */
.team-band{left:0;top:1954px;width:1200px;height:546px;background:var(--grey)}
.team-text{left:162px;top:2058px;width:450px}
.team-text .title{height:56px;margin:8px 0 18px}
.team-text h3{font-size:18.5px;line-height:32px;font-weight:400;color:var(--ink);margin-bottom:18px;letter-spacing:.3px}
.join-btn{display:inline-block;margin-top:22px;border:1px solid var(--dark);width:113px;height:41px;line-height:39px;text-align:center;font-size:13.5px;color:var(--ink)}
.team-photo{left:659px;top:2044px;width:380px;height:366px;background:radial-gradient(circle at 40% 45%,#e4c2a8,#b08a70 55%,#6b5a4c)}

/* stats */
.stats{left:150px;top:2578px;display:flex}
.stat{width:249px;text-align:center;position:relative}
.stat+.stat::before{content:"";position:absolute;left:0;top:30px;height:80px;border-left:1px dashed var(--line)}
.stat .glyph{position:relative;width:70px;height:70px;margin:0 auto}
.stat .glyph::before{content:"";position:absolute;left:-8px;top:-6px;width:44px;height:44px;border-radius:50%;background:#fdf3d0}
.stat .glyph svg{position:relative}
.stat .num{font-size:24px;margin-top:14px;color:var(--ink)}
.stat .lab{font-size:15.5px;color:#333;margin-top:4px}

/* footer */
.footer{left:0;top:2808px;width:1200px;height:451px;background:var(--grey)}
.f-head{font-size:18px;color:var(--ink)}
.quick{left:186px;top:2884px}
.quick ul{list-style:none;display:grid;grid-template-columns:146px 110px;row-gap:9px;margin-top:16px;font-size:13.5px;color:#555}
.quick li::before{content:"• "}
.f-brand{left:517px;top:2920px;display:flex;align-items:center;gap:10px}
.f-brand .sq{width:22px;height:22px;background:var(--yellow)}
.f-brand .nm{font-size:44px;color:var(--ink)}
.subscribe{left:748px;top:2884px;width:292px}
.subscribe p{margin:12px 0 14px;font-size:13.5px}
.sub-form{display:flex;height:34px;border:1px solid var(--line);background:var(--white)}
.sub-form .field{flex:1;font-size:13px;color:#aaa;padding:9px 12px}
.sub-form .go{width:74px;background:var(--yellow);color:var(--white);font-size:13px;display:flex;align-items:center;justify-content:center}
.rule{left:162px;width:876px;height:1px;background:var(--line)}
.contact{display:flex;align-items:center;gap:16px;font-size:13.5px;color:var(--ink)}
.contact b{display:block;font-weight:400;font-size:14.5px}
.copyright{left:0;top:3209px;width:1200px;text-align:center;font-size:13.5px;color:#444}
</style>
</head>
<body>

<header class="abs site-header">
  <div class="abs brand"><span class="brand-square"></span><span class="brand-name">Veralith</span></div>
  <nav class="abs main-nav">
    <span>Home</span><span class="active">About Us</span><span>Products</span><span>Our Technology</span><span>News</span><span>FAQ</span><span>Contact Us</span>
  </nav>
  <div class="abs search-tab"><span class="label">Search</span><span class="icon">
    <svg width="20" height="20" viewBox="0 0 20 20"><circle cx="9.5" cy="9.5" r="4" fill="none" stroke="#f6c400" stroke-width="1.4"/><line x1="12.5" y1="12.5" x2="15" y2="15" stroke="#f6c400" stroke-width="1.4"/></svg></span></div>
  <div class="abs buy-btn">Where to Buy</div>
</header>

<section class="abs hero" role="img" aria-label="Laboratory glass test tubes with a pipette dropping blue liquid">
  <h1>About Us</h1>
</section>
<div class="abs crumbs">Home<b>/</b>About Us</div>

<div class="abs grey-band"></div>
<div class="abs about-photo" role="img" aria-label="Stainless steel production line with a walkway between machines"></div>
<div class="abs about-text">
  <div class="eyebrow">A Few Words</div>
  <h2 class="title"><span>About Us</span></h2>
  <p>Our US company was formed to take advantage of 20 years of experience with Titanium Dioxide coatings in Japan. Our team is focused on real world solutions that are useful for cleaning surfaces in real time. The typical existing approaches to cleaning surfaces are temporary. They are not continuously active over long periods of time, and require constant maintenance or reapplication to keep protecting the surface.</p>
  <p>Today’s use of harsh chemicals, UV-C lighting, and other direct interventions can be expensive and ineffective. It also means that the moment you stop cleaning and re-introduce any contamination to the environment, the area is once again contaminated and will need cleaning again. This is not a sustainable or reliable method of protection.</p>
</div>
<div class="abs col-left">
  <p>Veralith offers a unique solution with our Japanese engineering team that utilizes Titanium Dioxide (TiO2) and light to actively break down microorganisms or any organic matter in real time on a molecule level. New formulas contain additives that additionally allow Veralith to work in the dark, enabling a full 24 hours a day protection.</p>
  <p>The traditional use of competing TiO2 coatings has always been to apply them to surfaces using organic binders, which has a major drawback as TiO2 breaks down this organic binder when light is applied to the surface, causing it to flake off the surface over time. This makes these solutions inefficient, since constant reapplication will be required.</p>
  <p>Veralith’s photocatalyst powered surfaces act quickly and last a long time, providing the best ROI in the industry for keeping your surfaces clean and protected.</p>
</div>
<div class="abs col-right">
  <p>Veralith uses a unique inorganic binder which permanently attaches the coating to any solid surface (even PTFE/Fluoroline). The hardness of the finished coating is comparable to Corvane glass screen protectors, and it lasts for years — unless physically removed or overpainted. It does not require any specific maintenance and it is optically clear. Veralith is the world’s first permanent cleaning Titanium Dioxide coating with an inorganic binder.</p>
  <p>The applications for this material are truly endless. Veralith can also be used as an active deodorizing and self-cleaning solution, or a permanent exterior surface cleaner.</p>
  <p>We look forward to discussing your applications today.</p>
</div>

<div class="abs features">
  <div class="card"><div class="badge"><svg width="44" height="40" viewBox="0 0 44 40" fill="none" stroke="#1c1c1c" stroke-width="1.6"><circle cx="22" cy="10" r="5"/><circle cx="10" cy="15" r="4"/><circle cx="34" cy="15" r="4"/><path d="M13 34v-6a9 9 0 0 1 18 0v6z"/><path d="M3 34v-4a7 7 0 0 1 10-6"/><path d="M41 34v-4a7 7 0 0 0-10-6"/></svg></div><small>Great People</small><strong>Our team is ready to serve you.</strong></div>
  <div class="card"><div class="badge"><svg width="44" height="44" viewBox="0 0 44 44" fill="none" stroke="#1c1c1c" stroke-width="1.6"><circle cx="22" cy="22" r="18"/><path d="M14 32c6-6 10-12 14-20"/><path d="M20 24c-4 0-6-3-6-6 3 0 6 2 6 6zM24 18c0-4 2-6 5-6 0 3-2 6-5 6z"/><line x1="9" y1="35" x2="35" y2="9"/></svg></div><small>Safe Products</small><strong>Harmless to Humans and Animals</strong></div>
  <div class="card"><div class="badge"><svg width="40" height="46" viewBox="0 0 40 46" fill="none" stroke="#1c1c1c" stroke-width="1.6"><circle cx="20" cy="17" r="13"/><circle cx="20" cy="17" r="8"/><path d="M11 27l-6 13 6-2 3 5 5-11M29 27l6 13-6-2-3 5-5-11"/></svg></div><small>Experience</small><strong>More than two decades of Experience</strong></div>
  <div class="card"><div class="badge"><svg width="48" height="34" viewBox="0 0 48 34" fill="none" stroke="#1c1c1c" stroke-width="1.6"><path d="M2 10l8-6 8 4 6-3 6 3 8-4 8 6-6 10-12 10-10-8"/><path d="M18 8l-6 7 4 3 8-6"/></svg></div><small>Projects</small><strong>Many successful projects completed</strong></div>
</div>

<div class="abs team-band"></div>
<div class="abs team-text">
  <div class="eyebrow">Our Advantage is Clear</div>
  <h2 class="title"><span>Our Team Wins</span></h2>
  <h3>Our team loves what they do, and that is what makes us unique.</h3>
  <p>Contact us to learn how you can become part of our exclusive team. Veralith is looking for good people to grow with us. We look forward to listening to our customers and team members to make us better.</p>
  <span class="join-btn">Join Now</span>
</div>
<div class="abs team-photo" role="img" aria-label="A group of team members joining fists together in a circle"></div>

<div class="abs stats">
  <div class="stat"><div class="glyph"><svg width="50" height="50" viewBox="0 0 50 50" fill="none" stroke="#f6c400" stroke-width="2"><path d="M6 16l6-10h26l6 10v28H6z"/><line x1="6" y1="16" x2="44" y2="16"/><path d="M21 6v14h8V6"/><line x1="30" y1="38" x2="38" y2="38"/></svg></div><div class="num">03</div><div class="lab">Products</div></div>
  <div class="stat"><div class="glyph"><svg width="50" height="56" viewBox="0 0 50 56" fill="none" stroke="#f6c400" stroke-width="2"><rect x="10" y="4" width="30" height="30"/><line x1="16" y1="12" x2="34" y2="12"/><line x1="16" y1="18" x2="34" y2="18"/><path d="M4 40l10-6 10 4 6-3 10 5-8 10-10 4-10-6z"/></svg></div><div class="num">150</div><div class="lab">Projects Completed</div></div>
  <div class="stat"><div class="glyph"><svg width="72" height="50" viewBox="0 0 72 50" fill="none" stroke="#f6c400" stroke-width="2"><circle cx="36" cy="12" r="8"/><circle cx="18" cy="18" r="6"/><circle cx="54" cy="18" r="6"/><path d="M22 46v-8a14 14 0 0 1 28 0v8z"/><path d="M6 46v-6a11 11 0 0 1 16-8M66 46v-6a11 11 0 0 0-16-8"/></svg></div><div class="num">28</div><div class="lab">Happy Clients</div></div>
  <div class="stat"><div class="glyph"><svg width="60" height="60" viewBox="0 0 60 60" fill="none" stroke="#f6c400" stroke-width="2"><circle cx="30" cy="22" r="16"/><path d="M30 12l3 7 7 .5-5.5 4.5 2 7-6.5-4-6.5 4 2-7-5.5-4.5 7-.5z"/><path d="M19 34l-9 16 7-2 4 6 7-14M41 34l9 16-7-2-4 6-7-14"/></svg></div><div class="num">08</div><div class="lab">Years of Experience</div></div>
</div>

<footer class="abs footer"></footer>
<div class="abs quick">
  <div class="f-head">Quick Links</div>
  <ul><li>Home</li><li>News</li><li>About Us</li><li>FAQ</li><li>Products</li><li>Contact Us</li><li>Our Technology</li><li>Where to Buy</li></ul>
</div>
<div class="abs f-brand"><span class="sq"></span><span class="nm">Veralith</span></div>
<div class="abs subscribe">
  <div class="f-head">Subscribe Today For New Updates</div>
  <p>Subscribe to our mailing list to get the updates to your email inbox....</p>
  <div class="sub-form"><span class="field">Email Address</span><span class="go">Sign Up</span></div>
</div>
<div class="abs rule" style="top:3058px"></div>
<div class="abs contact" style="left:186px;top:3093px"><svg width="24" height="26" viewBox="0 0 24 26" fill="none" stroke="#f6c400" stroke-width="1.6"><path d="M12 24s8-8 8-14a8 8 0 0 0-16 0c0 6 8 14 8 14z"/><circle cx="12" cy="10" r="3"/></svg><div><b>Address</b>Elmbrook, CT USA</div></div>
<div class="abs contact" style="left:516px;top:3093px"><svg width="24" height="26" viewBox="0 0 24 26" fill="none" stroke="#f6c400" stroke-width="1.6"><path d="M5 3l4 1 2 5-3 2a12 12 0 0 0 6 6l2-3 5 2 1 4c-1 2-3 3-5 3C9 22 2 15 2 7c0-2 1-4 3-4z"/></svg><div><b>Phone</b>555-018-2244</div></div>
<div class="abs contact" style="left:746px;top:3093px"><svg width="24" height="26" viewBox="0 0 24 26" fill="none" stroke="#f6c400" stroke-width="1.6"><path d="M2 10l10-7 10 7v13H2z"/><path d="M2 10l10 7 10-7"/></svg><div><b>Email</b>hello@veralith-mail.com</div></div>
<div class="abs rule" style="top:3170px"></div>
<div class="abs copyright">Copyright © 2022 Veralith, Inc. All Rights Reserved.</div>

</body>
</html>
```